Pitch Deck for KVR Forum 2025

Transform the current pitch deck into a visually compelling, modern, and highly engaging presentation that effectively communicates the value of Lattice Writ + KVR Manuals. The deck should feel professional, polished, and easy to digest with clean visuals, icons, and structured layouts.

Target Market(s)

Our audience includes enterprise decision-makers, content strategists, IT leaders, and digital transformation professionals who are considering Tovrin Insight Builder (KVR) Manuals and structured content solutions. They value efficiency, automation, AI-readiness, and compliance in content management. 👥 Who is the Target Market? Industries: Finance, Healthcare, Technology, Aerospace, and Large Enterprises. Roles: CIOs, Content Managers, Technical Writers, Digital Transformation Leads, Compliance Officers. Pain Points: Inefficient content workflows, compliance challenges, high translation costs, slow go-to-market content updates.

Industry/Entity Type

We operate in the structured content and AI-powered content management space, helping enterprises optimize content for automation, compliance, and personalization. Our work aligns with digital transformation strategies for large organizations needing scalable, AI-ready documentation solutions.

Font styles to use
Sans Serif
Other font styles liked:
• Poppins for headings

Requirements
Must have
• Must-Haves (My project must have…) Graphics from our existing banner: The pitch deck should incorporate the colours and visual elements from the banner we previously designed for consistency. A clean, modern design: White background with a balanced use of our brand colours. Icons & images: Use icons to represent key concepts instead of dense bullet points. Minimal text per slide: Key messages should be visual and concise. Strong visual hierarchy: Important points should be easy to scan and comprehend. Clear CTA on the final slide: A well-designed "Next Steps" section with contact information and a call-to-action.
Nice to have
• Diagrams & workflows: Simple, easy-to-follow visual representations of our processes. Subtle textures or accents: Avoid flat, heavy colour blocks, but light background gradients or design accents could work. Dynamic transitions: Smooth but professional slide animations that help guide the viewer. Typography hierarchy: Headings that stand out, but with a clean and professional font choice. Real-world mockups: Screenshots or abstract representations of KVR Manuals in action. Branded infographic elements: Visually engaging ways to present statistics and benefits.
Should not have
• Overly dark backgrounds: Most slides should remain white for readability and professionalism. Too much text per slide: We don’t want slides overloaded with text—focus on visuals. Generic stock images: Use purposeful, industry-relevant visuals that support the messaging. Excessive colours: Keep it consistent with the banner design—not too many competing colours. Complex animations: We want smooth, subtle transitions, but not over-the-top effects.

```html
<!DOCTYPE html>
<html lang="en">
<head>
<meta charset="utf-8">
<title>Lattice Writ + KVR Manuals — Pitch Deck</title>
<link href="https://fonts.googleapis.com/css2?family=Poppins:wght@400;500;600;700&display=swap" rel="stylesheet">
<style>
  :root{
    --orange:#f47a38;
    --blue:#5a9ad8;
    --ink:#1d1d1f;
    --grey:#6b6b70;
    --dark:#222224;
    --brand:#2c37b0;
    --purple:#8d3fa5;
    --coral:#f06a5a;
    --bg:#e8e8ea;
    --white:#ffffff;
  }
  *{box-sizing:border-box;margin:0;padding:0}
  html,body{width:1200px;height:1043px;overflow:hidden}
  body{background:var(--bg);font-family:"Poppins",sans-serif;color:var(--ink);position:relative}
  .slide{position:absolute;width:531px;height:299px;background:var(--white);overflow:hidden;box-shadow:0 2px 6px rgba(0,0,0,.12)}
  .s1{left:56px;top:50px}.s2{left:612px;top:50px}
  .s3{left:56px;top:375px}.s4{left:612px;top:375px}
  .s5{left:56px;top:694px}.s6{left:612px;top:694px}
  .abs{position:absolute}

  /* brand mark */
  .brand{display:flex;align-items:center;gap:6px;color:var(--brand);font-weight:600;line-height:1}
  .brand .dot{border-radius:50%;background:var(--brand);display:block}
  .brand-lg{left:31px;top:24px;font-size:15px}
  .brand-lg .dot{width:20px;height:20px}

  /* footer */
  .footer{left:17px;top:272px;width:500px;height:14px;display:flex;align-items:center;gap:4px}
  .footer .brand{font-size:7px}
  .footer .brand .dot{width:12px;height:12px}
  .footer .rule{flex:1;height:1px;background:var(--ink)}
  .footer .num{font-size:6px;margin-left:6px}

  /* cover */
  .cover-band{left:0;top:73px;width:531px;height:172px;background:var(--dark)}
  .cover-title{left:25px;top:42px;color:var(--white);font-weight:600;font-size:17px;line-height:1.35}
  .cover-title .big{font-size:22px;font-weight:700}
  .orange{color:var(--orange)}
  .blue{color:var(--blue)}
  .cover-sub{left:25px;top:128px;color:var(--white);font-size:8px;font-weight:600}
  .cover-art{left:325px;top:25px;width:200px;height:147px;border-radius:8px;background:linear-gradient(135deg,#3a3a3e 0%,#2d2d31 40%,#e46a8a 60%,#4dbf8d 75%,#f4934e 100%);opacity:.85}

  /* section divider */
  .ring{left:93px;top:43px;width:208px;height:208px}
  .ring-photo{left:102px;top:52px;width:190px;height:190px;border-radius:50%;background:radial-gradient(circle at 55% 40%,#f5d2c8 0%,#6a8fd0 22%,#203f86 55%,#0b1838 100%)}
  .badge{left:75px;top:124px;width:46px;height:46px;border-radius:50%;background:var(--white);border:3px solid var(--purple);display:flex;align-items:center;justify-content:center;font-weight:700;font-size:22px}
  .title-card{left:258px;top:108px;width:201px;height:77px;background:var(--white);box-shadow:0 2px 6px rgba(0,0,0,.15);padding:7px 0 0 18px;font-weight:700;font-size:15.5px;line-height:1.3}
  .title-card::before{content:"";position:absolute;left:0;top:0;width:8px;height:100%;background:linear-gradient(var(--purple),var(--coral))}
  .s5 .title-card{top:108px;width:201px}

  /* text slides */
  .h-lg{font-weight:700;font-size:17px;line-height:1.2}
  .body{font-size:6.6px;color:var(--grey);line-height:1.45}
  .body b{color:var(--ink);font-weight:600}
  .photo{border-radius:1px}
  .list-h{font-weight:600;font-size:8px}
  .checks{list-style:none}
  .checks li{position:relative;padding-left:11px;font-size:6.6px;height:14px;line-height:8px;color:var(--ink)}
  .checks li b{font-weight:600}
  .checks li::before{content:"";position:absolute;left:0;top:1px;width:6px;height:6px;border:1px solid var(--orange)}
  .checks li::after{content:"";position:absolute;left:2px;top:1px;width:2.5px;height:4.5px;border:solid var(--orange);border-width:0 1.2px 1.2px 0;transform:rotate(40deg)}

  .trust-box{left:41px;top:134px;width:437px;height:70px;border-radius:10px;background:var(--dark);padding:9px 16px 0 12px}
  .trust-box .checks li{color:var(--white);height:auto;margin-bottom:8px;line-height:1.35}
  .trust-box .checks li::before{border-color:var(--orange)}
  .closing{font-size:9.6px;line-height:1}
</style>
</head>
<body>

<!-- Cover -->
<section class="slide s1">
  <div class="abs brand brand-lg"><span class="dot"></span>Lattice Writ</div>
  <div class="abs cover-band">
    <h1 class="abs cover-title">The Future of<br><span class="big orange">Content is Structured</span><br><span class="big">&amp; <span class="blue">AI-Read</span></span></h1>
    <p class="abs cover-sub">Lattice Writ + KVR Manuals = Content you can trust.</p>
    <div class="abs cover-art" role="img" aria-label="Isometric illustration of stacked coloured blocks with documents and tech icons"></div>
  </div>
</section>

<!-- Section 01 -->
<section class="slide s2">
  <svg class="abs ring" viewBox="0 0 208 208" aria-hidden="true">
    <defs><linearGradient id="ringGrad1" x1="0" y1="0" x2="0" y2="1"><stop offset="0" stop-color="#8d3fa5"/><stop offset="1" stop-color="#f06a5a"/></linearGradient></defs>
    <circle cx="104" cy="104" r="101" fill="none" stroke="url(#ringGrad1)" stroke-width="5"/>
  </svg>
  <div class="abs ring-photo" role="img" aria-label="Robotic hand and human hand reaching toward a glowing light bulb"></div>
  <div class="abs badge">01</div>
  <h2 class="abs title-card"><span class="orange">The Problem:</span><br>Traditional Content<br>Is <span class="blue">In Crisis</span></h2>
  <footer class="abs footer"><span class="brand"><span class="dot"></span>Lattice Writ</span><span class="rule"></span><span class="num">2</span></footer>
</section>

<!-- Old way -->
<section class="slide s3">
  <h2 class="abs h-lg" style="left:37px;top:22px">The <span class="orange">Old Way</span><br><span class="blue">Won’t Get You</span> There</h2>
  <p class="abs body" style="left:38px;top:67px;width:460px"><b>The Content Crisis -</b> Traditional content management no longer works. Static, unstructured content traps information in silos, stifles innovation, and blocks scalability.</p>
  <p class="abs body" style="left:38px;top:91px;color:var(--ink)">AI, automation, and personalization demand structured intelligent content—now!</p>
  <div class="abs photo" style="left:38px;top:110px;width:116px;height:119px;background:linear-gradient(135deg,#c9cdd3,#8a8f98 55%,#3d4149)" role="img" aria-label="Two business professionals working at a laptop in an office"></div>
  <h3 class="abs list-h" style="left:161px;top:115px">Why the Old Way is Holding You Back?</h3>
  <ul class="abs checks" style="left:161px;top:131px">
    <li><b>Content inconsistency –</b> Unstructured, unpredictable formatting-dependent authoring</li>
    <li><b>Compliance challenges –</b> No audit trail, high exposure</li>
    <li><b>Limited content reuse –</b> Hard to repurpose, redundant wasted effort</li>
    <li><b>High translation costs –</b> Inefficient processes, high expenses</li>
    <li><b>Manual publishing workflow –</b> Slow, inefficient resource intensive</li>
    <li><b>Poor searchability –</b> Wasted time, frustrated users</li>
    <li><b>Lack of AI readiness –</b> Unable to power automation or chatbots</li>
  </ul>
  <p class="abs body" style="left:38px;top:237px;width:460px"><b>The Cost of Inaction:</b> Organizations that fail to structure and optimize their content fall behind, lose efficiency, and waste money on outdated processes.</p>
  <footer class="abs footer"><span class="brand"><span class="dot"></span>Lattice Writ</span><span class="rule"></span><span class="num">3</span></footer>
</section>

<!-- Cost -->
<section class="slide s4">
  <h2 class="abs" style="left:29px;top:16px;font-size:10.5px;font-weight:600">The Cost of Outdated, Unstructured Content</h2>
  <p class="abs body" style="left:29px;top:33px;width:460px">Traditional content management no longer works. <b>AI, automation, and personalization demand structured, intelligent content—now!</b> But without a modern content strategy, organizations face <b>rising costs, compliance risks, and operational inefficiencies that hold them back.</b></p>
  <p class="abs body" style="left:29px;top:65px;width:460px">Every delay, manual process, and inconsistency adds friction, <b>driving up costs and slowing your business down.</b> If your content isn’t structured and optimized, you’re losing time, money, and competitive advantage.</p>
  <h3 class="abs list-h" style="left:29px;top:92px">Here’s what it’s costing you:</h3>
  <div class="abs photo" style="left:29px;top:106px;width:145px;height:122px;background:linear-gradient(135deg,#d8dde3,#9aa7b8 50%,#4a5a75)" role="img" aria-label="Team meeting around a table with laptops"></div>
  <ul class="abs checks" style="left:182px;top:107px">
    <li><b>Delayed go-to-market, missed revenue opportunities – Slow content updates</b></li>
    <li><b>Millions lost in wasted resources – Inefficient workflows</b></li>
    <li><b>Regulatory exposure, potential fines – Compliance risks with no audit trail</b></li>
    <li><b>Inconsistent quality, poor user experience – Unstructured, formatting-dependent authoring</b></li>
    <li><b>Increased costs, redundant effort – Limited content reuse</b></li>
    <li><b>Excessive expenses, inefficiency – High translation costs</b></li>
    <li><b>Slow, resource-intensive operations – Manual publishing workflow</b></li>
    <li><b>Wasted time, frustrated employees – Poor searchability</b></li>
    <li><b>Unable to power automation, chatbots, and future innovations – Lack of AI readiness</b></li>
  </ul>
  <p class="abs body" style="left:29px;top:237px;width:470px"><b>It’s time to eliminate these roadblocks.</b> With the right content strategy, you can streamline operations, reduce risk, and <b>unlock the full potential of AI-driven automation.</b></p>
  <footer class="abs footer"><span class="brand"><span class="dot"></span>Lattice Writ</span><span class="rule"></span><span class="num">4</span></footer>
</section>

<!-- Section 02 -->
<section class="slide s5">
  <svg class="abs ring" viewBox="0 0 208 208" aria-hidden="true">
    <defs><linearGradient id="ringGrad2" x1="0" y1="0" x2="0" y2="1"><stop offset="0" stop-color="#8d3fa5"/><stop offset="1" stop-color="#f06a5a"/></linearGradient></defs>
    <circle cx="104" cy="104" r="101" fill="none" stroke="url(#ringGrad2)" stroke-width="5"/>
  </svg>
  <div class="abs ring-photo" role="img" aria-label="Robotic hand and human hand reaching toward a glowing light bulb"></div>
  <div class="abs badge">02</div>
  <h2 class="abs title-card"><span class="orange">The Shift:</span><br>AI has Changed<br>the <span class="blue">Content Game</span></h2>
  <footer class="abs footer"><span class="brand"><span class="dot"></span>Lattice Writ</span><span class="rule"></span><span class="num">5</span></footer>
</section>

<!-- Trust -->
<section class="slide s6">
  <h2 class="abs h-lg" style="left:31px;top:15px;line-height:1.24"><span class="orange">Your Users</span><br>Need Trust - A Single Source of Truth is<br><span class="blue">No Longer Optional</span></h2>
  <p class="abs" style="left:31px;top:84px;width:460px;font-size:9.6px;color:var(--grey);line-height:1.35">We are entering a defining moment. AI’s potential and consumer expecations are no longer theoretical—AI is reshaping business today. But without a trusted, structured foundation, AI creates more uncertainty than value.</p>
  <div class="abs trust-box">
    <ul class="checks">
      <li><b>Trust requires a single source of truth –</b> Inconsistent, unstructured content leads to misinformation and compliance risks</li>
      <li><b>Transparency demands structure –</b> AI-driven decisions depend on reliable, governed content</li>
      <li><b>Measurable ROI starts with accuracy –</b> AI is only as good as the content feeding it.</li>
    </ul>
  </div>
  <p class="abs closing" style="left:32px;top:222px">Lattice Writ + KVR Manuals = AI-ready content you can trust.</p>
  <p class="abs closing" style="left:32px;top:240px">The question isn’t IF you should prepare your content for AI—it’s HOW FAST you can do it.</p>
  <footer class="abs footer"><span class="brand"><span class="dot"></span>Lattice Writ</span><span class="rule"></span><span class="num">6</span></footer>
</section>

</body>
</html>
```